Business Card for Quillmark Ledger - A cannabis publication for executives.

I'd like some business cards for Quillmark Ledger. The logo is done (great job!) and I need a card design I will use with PRINTLY. I made it a short project to allow time for printing before an event. These will be standard sized cards (final artwork size 3.66" x 2.16" at 300dpi) with a final card size of 3.5" x 2.0". (See PRINTLY.com if you need more info.) I might try rounded corners but am not sure yet. I think the design will work okay with rounded.

Quillmark Ledger will be a bi-weekly publication for the cannabis industry. It is targeted to investors and industry executives, not consumers or pot smokers. So our market is more B2B. However I am open to creativity and making the card something people remark on.

My contact for card:

Dana Merrow
Founder/CEO
dana@quillmarkledger.example

2740 Harlow Avenue
Boston MA 02135
(617)555-0194

Target Market(s)

Executives, Industry people and investors in the Cannabis sector.

Contact Information for Business Card

PRINTLY does do double sided and the second side can be the same or different images. Only one side is required but use of the second side would be a bonus.

Font styles to use
Serif
Sans Serif
Decorative

Colors

Designer to choose colors to be used in the design.

Requirements
Must have
• Logo, contact info
Nice to have
• Style and design to make the card stand out in a crowd.

```html
<!DOCTYPE html>
<html lang="en">
<head>
<meta charset="utf-8">
<title>Quillmark Ledger – Business Card Concepts</title>
<link rel="stylesheet" href="https://fonts.googleapis.com/css2?family=Source+Sans+3:wght@400;600;700&family=Noto+Serif:ital,wght@1,700&display=swap">
<style>
  :root{
    --green:#86ad34;
    --blue:#1273bb;
    --mist:#e1ecf7;
    --mist-edge:#d3e3f4;
    --paper:#ffffff;
    --ink:#2b2b2b;
  }
  html,body{margin:0;padding:0;overflow:hidden;}
  body{width:849px;height:1200px;background:var(--paper);}
  .sheet{display:block;width:849px;height:1200px;}

  .cloud-path{vector-effect:non-scaling-stroke;}
  .paper{fill:var(--paper);}
  .fill-green{fill:var(--green);}
  .fill-blue{fill:var(--blue);}
  .fill-mist{fill:var(--mist);}
  .edge-ink{stroke:var(--ink);stroke-width:1.2;}
  .edge-green{stroke:var(--green);stroke-width:4;}
  .edge-blue{stroke:var(--blue);stroke-width:4;}
  .edge-mist{stroke:var(--mist-edge);stroke-width:6;}
  .inset{fill:none;stroke-width:1.6;}
  .inset-white{stroke:var(--paper);}
  .inset-green{stroke:var(--green);}
  .inset-blue{stroke:var(--blue);}

  .wordmark{font-family:"Source Sans 3",sans-serif;font-weight:700;font-size:27px;text-anchor:middle;letter-spacing:-0.3px;}
  .wordmark-small{font-family:"Source Sans 3",sans-serif;font-weight:700;font-size:15px;text-anchor:middle;}
  .person-name{font-family:"Noto Serif",serif;font-style:italic;font-weight:700;font-size:17px;text-anchor:middle;}
  .person-role{font-family:"Source Sans 3",sans-serif;font-weight:400;font-size:11.5px;text-anchor:middle;fill:var(--ink);}
  .email{font-family:"Source Sans 3",sans-serif;font-weight:400;font-size:12.5px;fill:var(--ink);}
  .address{font-family:"Source Sans 3",sans-serif;font-weight:600;font-size:10.5px;}

  .t-white{fill:var(--paper);}
  .t-green{fill:var(--green);}
  .t-blue{fill:var(--blue);}
  .t-ink{fill:var(--ink);}
  .mark-square-blue{fill:var(--blue);}
  .mark-square-green{fill:var(--green);}
  .mark-square-white{fill:var(--paper);}
  .icon-white{fill:var(--paper);}
  .icon-blue{fill:var(--blue);}
  .icon-green{fill:var(--green);}
  .env-line{fill:none;stroke:var(--paper);stroke-width:1;}
</style>
</head>
<body>
<svg class="sheet" viewBox="0 0 849 1200" xmlns="http://www.w3.org/2000/svg" role="img" aria-label="Three colourways of a folded cloud-shaped business card for Quillmark Ledger, front and back">
  <defs>
    <path id="cloud" class="cloud-path" d="M22 158 Q0 158 0 136 L0 92 Q0 62 32 59 L78 56 Q102 54 106 32 Q112 0 146 0 L216 0 Q250 0 256 32 Q260 54 284 56 L330 59 Q362 62 362 92 L362 136 Q362 158 340 158 Z"/>
    <g id="icon-phone"><path d="M1 1.5 Q1 0 2.5 0 L3.5 0 L4.6 2.6 L3.4 3.6 Q4.4 5.6 6.4 6.6 L7.4 5.4 L10 6.5 L10 7.5 Q10 9 8.5 9 Q1 8.5 1 1.5 Z"/></g>
    <g id="icon-pin"><path d="M5 0 A4 4 0 0 1 9 4 Q9 6.5 5 10 Q1 6.5 1 4 A4 4 0 0 1 5 0 Z M5 2.4 A1.6 1.6 0 1 0 5 5.6 A1.6 1.6 0 1 0 5 2.4 Z" fill-rule="evenodd"/></g>
  </defs>

  <!-- ROW 1 : green -->
  <g class="card-front-top" transform="translate(34 236) scale(1 -1)">
    <use href="#cloud" class="fill-green edge-green"/>
    <use href="#cloud" class="inset inset-white" transform="translate(181 79) scale(.961 .911) translate(-181 -79)"/>
  </g>
  <text class="wordmark-small t-white" x="215" y="159">Quillmark Ledger</text>
  <g class="card-front-bottom" transform="translate(34 240)">
    <use href="#cloud" class="paper edge-ink"/>
    <use href="#cloud" class="inset inset-green" transform="translate(181 79) scale(.961 .911) translate(-181 -79)"/>
  </g>
  <rect class="mark-square-blue" x="96" y="320" width="22" height="22"/>
  <text class="wordmark t-blue" x="232" y="340">Quillmark Ledger</text>

  <g class="card-back-top" transform="translate(454 236) scale(1 -1)">
    <use href="#cloud" class="fill-green edge-green"/>
    <use href="#cloud" class="inset inset-white" transform="translate(181 79) scale(.961 .911) translate(-181 -79)"/>
  </g>
  <g class="address-block" transform="rotate(180 628 120)">
    <use href="#icon-pin" class="icon-white" transform="translate(564 98)"/>
    <text class="address t-white" x="578" y="107">2740 Harlow Avenue</text>
    <text class="address t-white" x="578" y="121">Boston MA 02135</text>
    <use href="#icon-phone" class="icon-white" transform="translate(564 127)"/>
    <text class="address t-white" x="578" y="135">(617)555-0194</text>
  </g>
  <g class="card-back-bottom" transform="translate(454 240)">
    <use href="#cloud" class="paper edge-ink"/>
    <use href="#cloud" class="inset inset-green" transform="translate(181 79) scale(.961 .911) translate(-181 -79)"/>
  </g>
  <text class="person-name t-blue" x="635" y="308">Dana Merrow</text>
  <text class="person-role" x="635" y="324">Founder/CEO</text>
  <g class="email-icon" transform="translate(497 367)"><rect class="icon-blue" width="13" height="9"/><polyline class="env-line" points="0.5,0.5 6.5,5 12.5,0.5"/></g>
  <text class="email" x="515" y="376">dana@quillmarkledger.example</text>

  <!-- ROW 2 : blue -->
  <g class="card-front-top" transform="translate(34 586) scale(1 -1)">
    <use href="#cloud" class="fill-blue edge-blue"/>
    <use href="#cloud" class="inset inset-white" transform="translate(181 79) scale(.961 .911) translate(-181 -79)"/>
  </g>
  <text class="wordmark-small t-white" x="215" y="509">Quillmark Ledger</text>
  <g class="card-front-bottom" transform="translate(34 589)">
    <use href="#cloud" class="paper edge-ink"/>
    <use href="#cloud" class="inset inset-blue" transform="translate(181 79) scale(.961 .911) translate(-181 -79)"/>
  </g>
  <rect class="mark-square-green" x="96" y="669" width="22" height="22"/>
  <text class="wordmark t-blue" x="232" y="689">Quillmark Ledger</text>

  <g class="card-back-top" transform="translate(454 586) scale(1 -1)">
    <use href="#cloud" class="fill-blue edge-blue"/>
    <use href="#cloud" class="inset inset-white" transform="translate(181 79) scale(.961 .911) translate(-181 -79)"/>
  </g>
  <g class="address-block" transform="rotate(180 628 470)">
    <use href="#icon-pin" class="icon-white" transform="translate(564 448)"/>
    <text class="address t-white" x="578" y="457">2740 Harlow Avenue</text>
    <text class="address t-white" x="578" y="471">Boston MA 02135</text>
    <use href="#icon-phone" class="icon-white" transform="translate(564 477)"/>
    <text class="address t-white" x="578" y="485">(617)555-0194</text>
  </g>
  <g class="card-back-bottom" transform="translate(454 589)">
    <use href="#cloud" class="paper edge-ink"/>
    <use href="#cloud" class="inset inset-blue" transform="translate(181 79) scale(.961 .911) translate(-181 -79)"/>
  </g>
  <text class="person-name t-green" x="635" y="657">Dana Merrow</text>
  <text class="person-role" x="635" y="673">Founder/CEO</text>
  <g class="email-icon" transform="translate(497 716)"><rect class="icon-green" width="13" height="9"/><polyline class="env-line" points="0.5,0.5 6.5,5 12.5,0.5"/></g>
  <text class="email" x="515" y="725">dana@quillmarkledger.example</text>

  <!-- ROW 3 : blue & mist -->
  <g class="card-front-top" transform="translate(34 957) scale(1 -1)">
    <use href="#cloud" class="fill-blue edge-blue"/>
    <use href="#cloud" class="inset inset-white" transform="translate(181 79) scale(.961 .911) translate(-181 -79)"/>
  </g>
  <text class="wordmark-small t-green" x="215" y="880">Quillmark Ledger</text>
  <g class="card-front-bottom" transform="translate(34 965)">
    <use href="#cloud" class="fill-blue edge-blue"/>
    <use href="#cloud" class="inset inset-white" transform="translate(181 79) scale(.961 .911) translate(-181 -79)"/>
  </g>
  <rect class="mark-square-green" x="96" y="1045" width="22" height="22"/>
  <text class="wordmark t-white" x="232" y="1065">Quillmark Ledger</text>

  <g class="card-back-top" transform="translate(454 957) scale(1 -1)">
    <use href="#cloud" class="fill-mist edge-mist"/>
    <use href="#cloud" class="inset inset-white" transform="translate(181 79) scale(.961 .911) translate(-181 -79)"/>
  </g>
  <g class="address-block" transform="rotate(180 628 841)">
    <use href="#icon-pin" class="icon-blue" transform="translate(564 819)"/>
    <text class="address t-ink" x="578" y="828">2740 Harlow Avenue</text>
    <text class="address t-ink" x="578" y="842">Boston MA 02135</text>
    <use href="#icon-phone" class="icon-blue" transform="translate(564 848)"/>
    <text class="address t-ink" x="578" y="856">(617)555-0194</text>
  </g>
  <g class="card-back-bottom" transform="translate(454 965)">
    <use href="#cloud" class="fill-mist edge-mist"/>
    <use href="#cloud" class="inset inset-white" transform="translate(181 79) scale(.961 .911) translate(-181 -79)"/>
  </g>
  <text class="person-name t-green" x="635" y="1033">Dana Merrow</text>
  <text class="person-role" x="635" y="1049">Founder/CEO</text>
  <g class="email-icon" transform="translate(497 1092)"><rect class="icon-green" width="13" height="9"/><polyline class="env-line" points="0.5,0.5 6.5,5 12.5,0.5"/></g>
  <text class="email" x="515" y="1101">dana@quillmarkledger.example</text>
</svg>
</body>
</html>
```